Creative Business Card for my Sail Boat.. Tide & Time

Going to order PLASTIC business cards for my boat.. she is a sailing vessel catamaran named Tide & Time..

Target Market(s)

to impress other boaters with a unique designed plastic card

Contact Information for Business Card

S/V Tide & Time
Captain Owen Harlow
harlow@owen.example
Mobile/WhatsApp 1-555-318-7062
www.sailtideandtime.example

Requirements
Must have
• Cool colors. logo.. and info in Business Card Details.. Thanks! Utilize clear or cloudy plastic in design. Thanks

```html
<!DOCTYPE html>
<html lang="en">
<head>
<meta charset="utf-8">
<title>Tide &amp; Time — Business Card</title>
<link rel="stylesheet" href="https://fonts.googleapis.com/css2?family=Montserrat:wght@300;400;800&display=swap">
<style>
  :root {
    --canvas: #ecebe9;
    --card-white: #ffffff;
    --band-brown: #55240f;
    --stone-grey: #b9b1aa;
    --text-light: #ffffff;
    --brand-grey: #c9c2bb;
    --accent-green: #2f9a44;
  }
  * { box-sizing: border-box; margin: 0; padding: 0; }
  html, body {
    width: 1200px; height: 892px; overflow: hidden;
    background: var(--canvas);
    font-family: "Montserrat", sans-serif;
  }
  .sheet {
    width: 1200px; height: 892px;
    display: flex; flex-direction: column; align-items: center; justify-content: center;
    gap: 30px;
  }
  .card {
    position: relative;
    width: 700px; height: 400px;
    background: var(--card-white);
    box-shadow: 0 6px 18px rgba(0,0,0,0.15);
    overflow: hidden;
  }
  .band {
    position: absolute; left: 0; right: 0;
    background: var(--band-brown);
    display: flex; flex-direction: column; align-items: center; justify-content: center;
    color: var(--text-light);
    text-align: center;
  }
  .brand {
    display: flex; align-items: center; gap: 12px;
    font-weight: 800; font-size: 38px; line-height: 1; letter-spacing: 0.5px;
  }
  .brand-dot {
    width: 22px; height: 22px; border-radius: 50%;
    background: var(--accent-green);
  }
  .front .band { top: 110px; height: 140px; }
  .front .brand { color: var(--brand-grey); margin-bottom: 12px; }
  .holder-name { font-weight: 800; font-size: 26px; letter-spacing: 1px; text-transform: uppercase; line-height: 1.1; }
  .holder-role { font-weight: 300; font-size: 17px; letter-spacing: 1.5px; text-transform: uppercase; line-height: 1.2; margin-top: 2px; }
  .contact {
    position: absolute; left: 0; right: 0; top: 256px; bottom: 0;
    background: var(--stone-grey);
    color: var(--text-light);
    display: flex; flex-direction: column; align-items: center; justify-content: center;
    font-weight: 400; font-size: 15px; line-height: 1.55; text-align: center;
  }
  .contact-icons { display: flex; gap: 6px; margin-bottom: 6px; }
  .contact-icons svg { width: 16px; height: 16px; }
  .back .band { top: 130px; height: 140px; }
  .back .brand { color: var(--text-light); }
  .back .brand-dot { background: var(--text-light); }
</style>
</head>
<body>
<main class="sheet">
  <section class="card front" aria-label="Card front">
    <div class="band">
      <div class="brand"><span>Tide &amp; Time</span><span class="brand-dot"></span></div>
      <p class="holder-name">Owen Harlow</p>
      <p class="holder-role">Captain</p>
    </div>
    <div class="contact">
      <div class="contact-icons">
        <svg viewBox="0 0 16 16" aria-label="Phone"><circle cx="8" cy="8" r="7.5" fill="#55240f"/><path d="M5.5 4.5l1.5 0 .6 2-1 .8a5 5 0 0 0 2.1 2.1l.8-1 2 .6v1.5c0 .5-.5.9-1 .8A6.5 6.5 0 0 1 4.7 5.5c-.1-.5.3-1 .8-1z" fill="#fff"/></svg>
        <svg viewBox="0 0 16 16" aria-label="Email"><circle cx="8" cy="8" r="7.5" fill="#55240f"/><rect x="4" y="5.2" width="8" height="5.6" rx="0.6" fill="#fff"/><path d="M4.3 5.5L8 8.4l3.7-2.9" stroke="#55240f" stroke-width="0.8" fill="none"/></svg>
        <svg viewBox="0 0 16 16" aria-label="Website"><circle cx="8" cy="8" r="7.5" fill="#55240f"/><circle cx="8" cy="8" r="4" stroke="#fff" stroke-width="0.9" fill="none"/><ellipse cx="8" cy="8" rx="1.8" ry="4" stroke="#fff" stroke-width="0.8" fill="none"/><line x1="4" y1="8" x2="12" y2="8" stroke="#fff" stroke-width="0.8"/></svg>
      </div>
      <p>1-555-318-7062</p>
      <p>harlow@owen.example</p>
      <p>www.sailtideandtime.example</p>
    </div>
  </section>

  <section class="card back" aria-label="Card back">
    <div class="band">
      <div class="brand"><span>Tide &amp; Time</span><span class="brand-dot"></span></div>
    </div>
  </section>
</main>
</body>
</html>
```